label for selfmade spirits, start-up, quality product

Hey there, my name is Tobias, I am 24 years old, living in the southwest of Germany. In the last two years I did experiment: I produced my own spirits. I used self-produced fruit and distilled it in my families small distillery. Distilling has been a tradition in my family, now I want to start my own production and sales. In our region distilling fruit is a tradition but it is in the hand of well-established families / producers. I am planning to establish a quality product with a modern design to focus more on younger people and to sell my spirits to bars, restaurants and private consumers. I did two varieties: "Jojo plum variety" and "Mirabelle de Nancy". (Mirabelle) I am looking for a label design. The bottles will have 0.7 liters, white glass (due to the clear color of the spirits), in a modern bottle: https://www.glasbruckhaus-beispiel.de/flaschen-und-glaeser/spirituosen/spirituosenflaschen/varna-417 , html taste: clear and noble fruit character in the nose, fine flavor of the respective fruit. During the distillation process I tried to capture the natural aroma of the fruit. Therefore, I did a 2nd distilation which is a special feature, that not everybody does. Jojo Zwetschgen Brand "/" Mirabelle de Nancy Brand "- I am also open for. The design can be: - simple and classy, ​​with a valuable appearance that shows in its font, which is the product itself 3 generations were involved in the production, my grandpa gave me important hints, .. I am so open for all ideas that could catch the target group. the label could be printed on either a white or cream label paper. If you have any questions don`t hesitate to contact me, I am looking forward to your suggestions! Cheers!

Target Market(s)

young adults, urban people, people with an interest in a high quality product, ars / restaurants / private customers

Font styles to use
Decorative
Script

Colors

Designer to choose colors to be used in the design.

Requirements
Must have
• So, there are some things that have been posted on the label, due to legal restrictions: - my address: Tobias Wernsdorfer, Lindenweg 14, 68412 Talheim - alcohol level: "alc. 42% vol." - capacity: "0.70 L"; size at least 4 mm - batch number: "L"; please leave an empty space to fill in by hand this information has not been discussed, but should not be too much in the foreground, nor attract to much attention.

```html
<!DOCTYPE html>
<html lang="de">
<head>
<meta charset="utf-8">
<title>Lumo Obstbrand – Label</title>
<link href="https://fonts.googleapis.com/css2?family=Tenor+Sans&display=swap" rel="stylesheet">
<style>
  :root {
    --backdrop: #e9e9e9;
    --paper: #f5ecd3;
    --paper-light: #faf4e4;
    --paper-shade: #efe1bd;
    --gold: #b8801c;
    --gold-line: #cfae62;
    --ink: #2b2420;
    --ink-soft: #5a4d40;
  }
  * { margin: 0; padding: 0; box-sizing: border-box; }
  html, body {
    width: 1200px; height: 1013px; overflow: hidden;
    background: var(--backdrop);
  }
  .canvas { position: relative; width: 1200px; height: 1013px; }
  .label {
    position: absolute; left: 150px; top: 90px;
    width: 900px; height: 834px;
    background: var(--paper);
    box-shadow: 0 4px 18px rgba(0,0,0,.12);
    font-family: "Tenor Sans", sans-serif;
  }
  .label__pattern {
    position: absolute; inset: 0;
    background: radial-gradient(ellipse at center, var(--paper-light) 0%, var(--paper) 60%, var(--paper-shade) 100%);
  }
  .label__frame {
    position: absolute; left: 30px; right: 30px; top: 30px; bottom: 40px;
    border: 3px solid var(--gold-line);
  }
  .label__frame::after {
    content: ""; position: absolute; inset: 10px;
    border: 1.5px solid var(--gold-line);
  }
  .label__line {
    position: absolute; left: 0; right: 0;
    text-align: center; white-space: nowrap;
  }
  .product-name {
    top: 110px;
    font-size: 170px; line-height: 1;
    letter-spacing: 12px;
    font-weight: 400;
    color: var(--gold);
  }
  .variety {
    top: 300px;
    font-size: 100px; line-height: 1;
    font-weight: 400;
    color: var(--gold);
  }
  .brand-name {
    top: 492px;
    font-size: 38px; letter-spacing: 1px;
    color: var(--ink);
  }
  .producer {
    top: 585px;
    font-size: 24px;
    color: var(--ink);
  }
  .facts {
    position: absolute; left: 0; right: 0; top: 640px;
    display: flex; justify-content: center; align-items: flex-start;
    color: var(--ink-soft);
  }
  .facts__item { padding: 8px 18px 0; font-size: 28px; white-space: nowrap; }
  .facts__item--batch { width: 230px; height: 76px; font-size: 24px; padding-top: 4px; color: var(--ink); }
  .facts__divider { width: 2px; height: 74px; background: var(--ink-soft); }
</style>
</head>
<body>
<main class="canvas">
  <section class="label">
    <div class="label__pattern" role="img" aria-label="Faint cream damask ornament pattern across the label"></div>
    <div class="label__frame"></div>
    <h1 class="label__line product-name">Lumo</h1>
    <p class="label__line variety">Obstbrand</p>
    <p class="label__line brand-name">BRAND NAME</p>
    <p class="label__line producer">Tobias Wernsdorfer, Lindenweg 14, 68412 Talheim</p>
    <div class="facts">
      <span class="facts__item">0,70 L</span>
      <span class="facts__divider"></span>
      <span class="facts__item facts__item--batch">Batch number:</span>
      <span class="facts__divider"></span>
      <span class="facts__item">Alc. 42% vol.</span>
    </div>
  </section>
</main>
</body>
</html>
```